Kestrel Gardenworks Business Card

An eye catching, yet simple business card that includes;

1. our logo
2. office phone - 5083172946
3. email - kestrelgardenworks@mailbrook.com
4. website - www.kestrelgardenworks.com
5. instagram - @kestrelgardenworksnv

```html
<!DOCTYPE html>
<html lang="en">
<head>
<meta charset="utf-8">
<title>Kestrel Gardenworks Business Card</title>
<link rel="stylesheet" href="https://fonts.googleapis.com/css2?family=Archivo+Black&family=Poppins:ital,wght@0,400;0,500;1,500&display=swap">
<style>
  :root {
    --page: #ece7e1;
    --card: #ffffff;
    --brown: #a0602c;
    --brown-dark: #7a4a26;
    --ink: #1d1a18;
    --band-end: #1e1917;
    --band-text: #ffffff;
  }
  * { margin: 0; padding: 0; box-sizing: border-box; }
  html, body {
    width: 1189px;
    height: 1200px;
    overflow: hidden;
    background: var(--page);
    font-family: "Poppins", sans-serif;
    color: var(--ink);
  }
  .card {
    position: absolute;
    left: 169px;
    width: 851px;
    height: 484px;
    background: var(--card);
    border-radius: 34px;
    box-shadow: 0 6px 18px rgba(60, 40, 20, 0.22);
    overflow: hidden;
  }
  .card--front { top: 112px; }
  .card--back { top: 641px; }

  .web-band {
    position: absolute;
    left: 0;
    top: 409px;
    width: 100%;
    height: 43px;
    background: linear-gradient(90deg, var(--brown) 0%, var(--brown-dark) 45%, var(--band-end) 100%);
    color: var(--band-text);
    font-size: 18px;
    letter-spacing: 6.5px;
    display: flex;
    align-items: center;
    justify-content: center;
  }

  .wordmark {
    position: absolute;
    font-family: "Archivo Black", sans-serif;
    color: var(--brown);
    line-height: 1;
    text-align: center;
    display: flex;
    flex-direction: column;
    align-items: center;
  }
  .wordmark__main { display: block; }
  .wordmark__sub { display: block; letter-spacing: 6px; }

  .card--front .wordmark {
    left: 0;
    width: 100%;
    top: 160px;
  }
  .card--front .wordmark__main { font-size: 72px; }
  .card--front .wordmark__sub { font-size: 34px; margin-top: 8px; }

  .card--back .wordmark {
    left: 30px;
    width: 355px;
    top: 192px;
  }
  .card--back .wordmark__main { font-size: 58px; }
  .card--back .wordmark__sub { font-size: 26px; margin-top: 6px; letter-spacing: 4px; }

  .divider {
    position: absolute;
    left: 409px;
    top: 163px;
    width: 2px;
    height: 159px;
    background: var(--brown);
  }

  .person {
    position: absolute;
    left: 439px;
    top: 164px;
  }
  .person__name {
    font-family: "Archivo Black", sans-serif;
    font-style: italic;
    font-size: 25px;
    color: var(--brown);
    line-height: 1.1;
  }
  .person__role {
    font-style: italic;
    font-weight: 500;
    font-size: 18px;
    line-height: 1.3;
  }

  .contacts {
    position: absolute;
    left: 439px;
    top: 236px;
    list-style: none;
  }
  .contacts__item {
    display: flex;
    align-items: center;
    gap: 8px;
    font-size: 19px;
    line-height: 27px;
  }
  .contacts__icon {
    width: 19px;
    height: 19px;
    flex: none;
  }
</style>
</head>
<body>

<section class="card card--front">
  <div class="wordmark">
    <span class="wordmark__main">KESTREL</span>
    <span class="wordmark__sub">GARDENWORKS</span>
  </div>
  <div class="web-band">www.kestrelgardenworks.com</div>
</section>

<section class="card card--back">
  <div class="wordmark">
    <span class="wordmark__main">KESTREL</span>
    <span class="wordmark__sub">GARDENWORKS</span>
  </div>

  <div class="divider"></div>

  <div class="person">
    <p class="person__name">Owen Hartley</p>
    <p class="person__role">Manager</p>
  </div>

  <ul class="contacts">
    <li class="contacts__item">
      <svg class="contacts__icon" viewBox="0 0 20 20" aria-hidden="true">
        <circle cx="10" cy="10" r="10" fill="#a0602c"/>
        <path d="M6.5 5.2c.6-.4 1.2-.2 1.5.3l.9 1.6c.3.5.1 1-.3 1.3l-.6.4c.5 1.2 1.5 2.2 2.7 2.7l.4-.6c.3-.4.8-.6 1.3-.3l1.6.9c.5.3.7.9.3 1.5-.6 1-1.6 1.4-2.6 1-2.6-1-4.6-3-5.6-5.6-.4-1 0-2 .4-2.6z" fill="#fff"/>
      </svg>
      <span>5083172946</span>
    </li>
    <li class="contacts__item">
      <svg class="contacts__icon" viewBox="0 0 20 20" aria-hidden="true">
        <circle cx="10" cy="10" r="10" fill="#a0602c"/>
        <rect x="5" y="6.5" width="10" height="7" rx="1" fill="#fff"/>
        <path d="M5.3 7l4.7 3.6L14.7 7" fill="none" stroke="#a0602c" stroke-width="1.1"/>
      </svg>
      <span>kestrelgardenworks@mailbrook.com</span>
    </li>
    <li class="contacts__item">
      <svg class="contacts__icon" viewBox="0 0 20 20" aria-hidden="true">
        <circle cx="10" cy="10" r="10" fill="#a0602c"/>
      </svg>
      <span>@kestrelgardenworksnv</span>
    </li>
  </ul>

  <div class="web-band">www.kestrelgardenworks.com</div>
</section>

</body>
</html>
```